Etikettendesign für Imkereiprodukt
Zielgruppe
Ich betreibe eine Imkerei nach ökologischen Gesichtspunkten und vertreibe alles rund um die Biene- Honig, Wachs, Met, Likör...
Aus Bienenwachs und reinem Leinöl stelle ich ein natürliches Holzwachs her. (Wachs stammt aus eigener Bio Imkerei, Leinöl wird in Deutschland hergestellt)
Mit dem Wachs werden unbehandelte Hölzer imprägniert, gegen Feuchtigkeit geschützt, das Wachs verleiht dem Holz einen matten Glanz
Für dieses Produkt benötige ich ein Etikett.
Aufgabenstellung
- rundes Etikett Durchmesser 85 mm
- Verwendung von eigenem Firmenlogo (Anhang) (Name der Imkerei auch 'Wabenritter')
- Verwendung von folgenden Textbausteinen:
'ausschließlich Leinöl und Bienenwachs'
'regional von Hand hergestellt'
'komplett ohne Lösungsmittel'
oder ähnlich
- Herstelleradresse
- Datei nach Druck-vorgaben

```html
<!DOCTYPE html>
<html lang="de">
<head>
<meta charset="utf-8">
<title>Wabenritter Holzwachs – Etikett</title>
<link rel="stylesheet" href="https://fonts.googleapis.com/css2?family=Alegreya+SC:wght@500&family=Fira+Sans+Condensed:wght@300;600;800&family=Rubik+Dirt&display=swap">
<style>
  :root {
    --page: #f5f5f5;
    --rim: #1e1d1b;
    --gold: #b59f63;
    --ink: #1e1d1b;
    --white: #ffffff;
  }
  html, body { margin: 0; padding: 0; overflow: hidden; }
  body { width: 1200px; height: 1199px; background: var(--page); position: relative; }
  .label { position: absolute; left: 340px; top: 115px; width: 535px; height: 535px; }
  .label-shape { position: absolute; inset: 0; }
  .label-content { position: absolute; inset: 0; text-align: center; color: var(--ink); }
  .brand-mark {
    position: absolute; left: 50%; top: 62px; width: 82px; height: 82px;
    margin-left: -41px; border-radius: 50%; background: var(--ink);
  }
  .brand-name {
    position: absolute; top: 182px; width: 100%; margin: 0;
    font-family: "Alegreya SC", serif; font-weight: 500;
    font-size: 22px; letter-spacing: 1.5px;
  }
  .product-name {
    position: absolute; top: 228px; width: 100%; margin: 0;
    font-family: "Rubik Dirt", sans-serif; font-size: 50px; font-weight: 400;
    color: var(--white); letter-spacing: 2px;
  }
  .product-claim {
    position: absolute; top: 287px; width: 100%; margin: 0;
    font-family: "Fira Sans Condensed", sans-serif; font-weight: 800;
    font-size: 14px; letter-spacing: 1.6px; text-transform: uppercase;
  }
  .product-facts {
    position: absolute; top: 320px; width: 100%; margin: 0; padding: 0; list-style: none;
    font-family: "Fira Sans Condensed", sans-serif; font-weight: 300;
    font-size: 16px; line-height: 20px;
  }
  .maker {
    position: absolute; top: 393px; width: 100%; margin: 0;
    font-family: "Fira Sans Condensed", sans-serif; font-weight: 600; font-style: normal;
    font-size: 13.5px; line-height: 17.5px; color: var(--white);
  }
</style>
</head>
<body>
  <div class="label">
    <svg class="label-shape" viewBox="0 0 535 535" role="img" aria-label="Holzscheibe mit Jahresringen als Etikettform">
      <ellipse cx="267" cy="267" rx="262" ry="262" fill="var(--rim)"/>
      <ellipse cx="266" cy="270" rx="242" ry="232" fill="var(--gold)"/>
    </svg>
    <div class="label-content">
      <span class="brand-mark" aria-hidden="true"></span>
      <p class="brand-name">WABENRITTER</p>
      <h1 class="product-name">HOLZWACHS</h1>
      <p class="product-claim">Regional von Hand hergestellt</p>
      <ul class="product-facts">
        <li>· ausschließlich Leinöl und Bienenwachs</li>
        <li>· komplett ohne Lösungsmittel</li>
      </ul>
      <address class="maker">Imkerei Wabenritter<br>Lindenweg 7, 34567 Wiesental<br>www.wabenritter-imkerei.de</address>
    </div>
  </div>
</body>
</html>
```